Bref créative
Larkfield Joint & Motion Medicine
Letterhead, stationary and card design
Professional
Dr. Paul Korvitz
Director
418 West 71st Street
New York, NY 10187
director@larkfieldjoint.com
larkfieldjoint.com
Here is the logo file for use with the project

```html
<!DOCTYPE html>
<html lang="en">
<head>
<meta charset="utf-8">
<title>Larkfield Joint &amp; Motion Medicine — Stationery</title>
<link href="https://fonts.googleapis.com/css2?family=Montserrat:wght@400;500;600&display=swap" rel="stylesheet">
<style>
  :root{
    --bg:#e6e6e4;
    --paper:#ffffff;
    --ink:#4a4a4a;
    --ink-soft:#7a7a7a;
    --accent:#e0922c;
    --rule:#c9c9c9;
    --shadow:rgba(0,0,0,.18);
  }
  *{box-sizing:border-box;margin:0;padding:0}
  html,body{width:1200px;height:840px;overflow:hidden}
  body{background:var(--bg);font-family:"Montserrat",Arial,sans-serif;color:var(--ink);position:relative}
  .sheet{position:absolute;background:var(--paper);box-shadow:0 4px 14px var(--shadow)}

  .brand{display:flex;align-items:center;gap:8px}
  .brand-dot{border-radius:50%;background:var(--accent);flex:none}
  .brand-name{font-weight:500;color:var(--ink);text-transform:uppercase;line-height:1.15;letter-spacing:.04em}

  /* Letterhead */
  .letterhead{left:110px;top:56px;width:520px;height:730px;padding:34px 40px}
  .letterhead .brand-dot{width:34px;height:34px}
  .letterhead .brand-name{font-size:13px;width:200px}
  .letter{margin-top:26px;font-size:8.4px;line-height:1.55;color:var(--ink-soft)}
  .letter p{margin-bottom:11px}
  .letter .source{color:var(--ink);margin-top:-8px}
  .letter .salute{color:var(--ink)}
  .letter-footer{position:absolute;left:40px;bottom:30px;font-size:7.5px;line-height:1.6;color:var(--ink-soft)}

  /* Envelope */
  .envelope{left:660px;top:84px;width:450px;height:236px;padding:22px 24px}
  .envelope .brand-dot{width:26px;height:26px}
  .envelope .brand-name{font-size:10px;width:170px}
  .return-address{font-size:6.5px;color:var(--ink-soft);margin-top:8px}
  .recipient{position:absolute;right:26px;top:60px;width:190px;height:120px;border:1px solid var(--rule);padding:10px 12px;font-size:8px;line-height:1.45;color:var(--ink)}

  /* Business cards */
  .card{top:452px;width:210px;height:124px}
  .card-front{left:688px;padding:14px 14px}
  .card-front .brand-dot{width:18px;height:18px}
  .card-front .brand-name{font-size:7.5px;width:130px}
  .card-contact{position:absolute;left:14px;bottom:14px;font-size:5.6px;line-height:1.6;color:var(--ink-soft)}
  .card-person{position:absolute;right:14px;bottom:62px;font-size:6px;color:var(--ink);text-align:left;width:78px;border-left:1px solid var(--rule);padding-left:6px}
  .card-person .role{color:var(--accent)}
  .card-back{left:912px;display:flex;flex-direction:column;align-items:center;justify-content:center}
  .card-back .brand-dot{width:24px;height:24px}
  .card-back .brand-name{font-size:8.5px;width:140px}
  .card-web{position:absolute;right:12px;bottom:10px;font-size:6px;color:var(--ink-soft)}
</style>
</head>
<body>

<section class="sheet letterhead">
  <div class="brand">
    <span class="brand-dot"></span>
    <span class="brand-name">Larkfield Joint &amp; Motion Medicine</span>
  </div>
  <div class="letter">
    <p class="salute">Dear<br>Someone Somebody,</p>
    <p>Thank you for choosing our clinic for your care. Our team of specialists works together to assess, treat and guide each patient through a clear plan of recovery. We focus on movement, strength and lasting comfort, and we take time to explain every step so you always know what comes next in your treatment and why it matters to you.</p>
    <p class="source">Clinic note 1.10 from the patient guide, reviewed by the care team</p>
    <p>Before your first visit, please bring any recent scans, a list of current medicines and a note of when your pain began. This helps us form an accurate picture quickly. Our front desk will confirm your time by phone one day ahead, and can answer questions about parking, forms and insurance cover at any point.</p>
    <p class="source">Visit guide 2.04, prepared by the front desk team</p>
    <p>After treatment we will send a short summary of your plan along with exercises to practise at home. Small daily steps make a real difference, and we will review your progress at each follow-up. If anything changes, call us and we will find a time that suits you as soon as we can.</p>
    <p class="source">Care summary 3.12, issued by the clinic director</p>
    <p class="salute">Yours Truly,<br>Dr. Paul Korvitz</p>
  </div>
  <div class="letter-footer">
    418 West 71st Street, New York, NY 10187<br>
    Phone: 212-555-0148 &nbsp; Fax: 212-555-0149<br>
    director@larkfieldjoint.com &nbsp; Web: larkfieldjoint.com
  </div>
</section>

<section class="sheet envelope">
  <div class="brand">
    <span class="brand-dot"></span>
    <span class="brand-name">Larkfield Joint &amp; Motion Medicine</span>
  </div>
  <p class="return-address">418 West 71st Street, New York, NY 10187</p>
  <div class="recipient">
    To:<br>
    Mr. Halden<br>
    111 Street No 111, Suit 222, City Name, State<br>
    Toll Free : 111-222-333<br>
    Cell : 111-222-333<br>
    Cell : 111-222-333<br>
    E-mail : mhalden@mail.com<br>
    Web : www.mhalden.com
  </div>
</section>

<section class="sheet card card-front">
  <div class="brand">
    <span class="brand-dot"></span>
    <span class="brand-name">Larkfield Joint &amp; Motion Medicine</span>
  </div>
  <div class="card-person">Dr. Paul Korvitz<br><span class="role">Director</span></div>
  <div class="card-contact">
    Phone: 212-555-0148<br>
    Fax: 212-555-0149<br>
    director@larkfieldjoint.com<br>
    larkfieldjoint.com<br>
    418 West 71st Street, New York, NY 10187
  </div>
</section>

<section class="sheet card card-back">
  <div class="brand">
    <span class="brand-dot"></span>
    <span class="brand-name">Larkfield Joint &amp; Motion Medicine</span>
  </div>
  <span class="card-web">larkfieldjoint.com</span>
</section>

</body>
</html>
```